Design graphics for 2" Safety Stickers

we are looking for a round (circle) safety sticker design with our logo on it.
these stickers are given to workers to stick on their hard hat. each sticker will have a common safety phrase like: Think Safety First, Safety is Job #1, Safety is Teamwork, etc.....these stickers are freebies to our customers.

Target Market(s)

our customers

Font styles to use
Sans Serif

```html
<!DOCTYPE html>
<html lang="en">
<head>
<meta charset="utf-8">
<title>Hard Hat Safety Stickers</title>
<link href="https://fonts.googleapis.com/css2?family=Archivo:wght@400;900&display=swap" rel="stylesheet">
<style>
  :root {
    --bg: #dadada;
    --bg-mid: #d4d4d4;
    --blue: #3f5aa0;
    --green: #2e8b4a;
    --white: #f4f4f4;
    --ink: #2b2b2b;
  }
  html, body {
    margin: 0;
    padding: 0;
    width: 1200px;
    height: 565px;
    overflow: hidden;
    background: var(--bg);
  }
  .sticker-sheet {
    display: flex;
    width: 1200px;
    height: 565px;
  }
  .sticker-panel {
    display: flex;
    align-items: center;
    justify-content: center;
    height: 565px;
  }
  .sticker-panel--teamwork { width: 375px; }
  .sticker-panel--job-one { width: 446px; background: var(--bg-mid); }
  .sticker-panel--think-first { width: 379px; }
  .sticker { width: 260px; height: 260px; }
  .phrase-bold { font-family: "Archivo", Arial, sans-serif; font-weight: 900; }
  .phrase-light { font-family: "Archivo", Arial, sans-serif; font-weight: 400; }
  .brand-name { font-family: "Archivo", Arial, sans-serif; font-weight: 900; fill: var(--ink); }
</style>
</head>
<body>
<main class="sticker-sheet">

  <!-- Safety is teamwork -->
  <section class="sticker-panel sticker-panel--teamwork">
    <svg class="sticker" viewBox="0 0 260 260" aria-label="Safety is teamwork sticker">
      <defs>
        <clipPath id="teamwork-disc"><circle cx="130" cy="130" r="126"/></clipPath>
      </defs>
      <g clip-path="url(#teamwork-disc)">
        <rect width="260" height="260" fill="var(--blue)"/>
        <circle cx="98" cy="48" r="48" fill="var(--white)"/>
      </g>
      <g transform="translate(72 58) rotate(-20)">
        <circle cx="0" cy="-5" r="7" fill="var(--blue)"/>
        <text class="brand-name" x="11" y="0" font-size="15">KESTREL</text>
      </g>
      <g transform="translate(56 178) rotate(-20)">
        <text class="phrase-bold" x="0" y="0" font-size="40" fill="var(--white)">SAFETY</text>
        <text x="14" y="36" font-size="26" fill="var(--green)"><tspan class="phrase-light">is</tspan><tspan class="phrase-bold" dx="4">teamwork</tspan></text>
      </g>
    </svg>
  </section>

  <!-- Safety is job #1 -->
  <section class="sticker-panel sticker-panel--job-one">
    <svg class="sticker" viewBox="0 0 260 260" aria-label="Safety is job number 1 sticker">
      <defs>
        <clipPath id="job-one-disc"><circle cx="130" cy="130" r="126"/></clipPath>
      </defs>
      <g clip-path="url(#job-one-disc)">
        <rect width="260" height="260" fill="var(--white)"/>
        <circle cx="228" cy="112" r="76" fill="var(--blue)"/>
      </g>
      <text class="phrase-bold" x="206" y="146" font-size="76" fill="var(--white)" transform="rotate(-12 206 146)">1</text>
      <g transform="translate(36 152) rotate(-18)">
        <text class="phrase-bold" x="0" y="0" font-size="30" fill="var(--green)">SAFETY</text>
        <text class="phrase-light" x="6" y="38" font-size="32" fill="var(--blue)">is job #</text>
      </g>
      <g transform="translate(124 218) rotate(-14)">
        <circle cx="0" cy="-5" r="7" fill="var(--blue)"/>
        <text class="brand-name" x="11" y="0" font-size="15">KESTREL</text>
      </g>
    </svg>
  </section>

  <!-- Think safety first -->
  <section class="sticker-panel sticker-panel--think-first">
    <svg class="sticker" viewBox="0 0 260 260" aria-label="Think safety first sticker">
      <circle cx="130" cy="130" r="126" fill="var(--green)"/>
      <g>
        <circle cx="92" cy="43" r="7" fill="var(--blue)"/>
        <text class="brand-name" x="103" y="48" font-size="15">KESTREL</text>
      </g>
      <text class="phrase-light" x="54" y="124" font-size="34" fill="var(--blue)">think</text>
      <text class="phrase-bold" x="54" y="158" font-size="34" fill="var(--white)">SAFETY</text>
      <text class="phrase-light" x="206" y="192" font-size="34" fill="var(--blue)" text-anchor="end">first</text>
    </svg>
  </section>

</main>
</body>
</html>
```